Wealth management Facebook Advertisement

Hello, we are trying to capture more leads to our online booking link through Facebook advertisement. We want an attractive modern design to get more clients and catch the attention of high net-worth clients. We deal with high-net-worth retirees, business owners, farmers, and wealth transfer. We offer high-net-worth client solutions that cover Financial Planning, Retirement and Estate Planning, Investment Planning, Tax Planning, and Insurance Planning. The final design that we would be looking for is modern and eye-catching and makes the prospective clients want to click our meeting link to schedule an introductory consultation.

We are in the Wealth Management / Financial Planning industry

Our online booking link Is the following :

https://bookings.qvnfinancial-demo.net/calendar/OliverBrandtAssociatesQLPrivateWealth@qvnfinancial-demo.net/bookings/

Our current Facebook page is the following:

https://www.sociopage-demo.net/BrandtPrivateWealth

Please ask any further questions for needed information for creating design

```html
<!DOCTYPE html>
<html lang="en">
<head>
<meta charset="utf-8">
<title>Holistic Financial Plan – Ad Banners</title>
<link rel="stylesheet" href="https://fonts.googleapis.com/css2?family=Oswald:wght@700&family=Montserrat:wght@300;400;600&display=swap">
<style>
  :root {
    --page-bg: #c9dff2;
    --navy: #0a2466;
    --navy-deep: #00205b;
    --brand-blue: #0077d4;
    --gradient-top: #0072d0;
    --gradient-bottom: #002a70;
    --white: #ffffff;
  }
  * { margin: 0; padding: 0; box-sizing: border-box; }
  html, body { width: 1200px; height: 1200px; overflow: hidden; }
  body {
    background: var(--page-bg);
    position: relative;
    font-family: "Montserrat", Arial, sans-serif;
  }
  .board-title {
    position: absolute;
    top: 118px;
    left: 0;
    width: 1200px;
    text-align: center;
    font-family: "Montserrat", Arial, sans-serif;
    font-weight: 400;
    font-size: 38px;
    letter-spacing: 37px;
    padding-left: 37px;
    color: var(--navy);
  }
  .banner-frame {
    position: absolute;
    left: 112px;
    width: 975px;
    height: 407px;
    box-shadow: 0 0 40px 12px rgba(255,255,255,0.55);
  }
  .banner-frame.first { top: 197px; }
  .banner-frame.second { top: 643px; }
  .banner {
    position: absolute;
    top: 0; left: 0;
    width: 1570px;
    height: 655px;
    background: var(--white);
    transform: scale(0.621);
    transform-origin: top left;
    overflow: hidden;
  }
  .banner-shapes { position: absolute; inset: 0; }
  .brand {
    position: absolute;
    left: 109px;
    top: 110px;
    display: flex;
    align-items: flex-start;
    gap: 10px;
  }
  .brand-square {
    width: 38px; height: 38px;
    background: var(--brand-blue);
    margin-top: 4px;
  }
  .brand-name {
    font-weight: 600;
    font-size: 15px;
    line-height: 16px;
    color: var(--navy);
    text-transform: uppercase;
  }
  .brand-name span { display: block; }
  .brand-name .gap { margin-top: 6px; }
  .headline {
    position: absolute;
    left: 106px;
    top: 196px;
    font-family: "Oswald", "Arial Narrow", sans-serif;
    font-weight: 700;
    text-transform: uppercase;
    line-height: 1;
    transform: scaleY(1.05);
    transform-origin: top left;
  }
  .headline-lead {
    display: block;
    font-size: 64px;
    color: var(--navy);
    letter-spacing: -0.5px;
  }
  .headline-main {
    display: block;
    font-size: 88px;
    color: var(--brand-blue);
    margin-top: -8px;
    letter-spacing: -0.5px;
  }
  .headline-rule {
    position: absolute;
    left: 109px;
    top: 349px;
    width: 613px;
    height: 2px;
    background: var(--navy);
  }
  .subline {
    position: absolute;
    left: 109px;
    top: 361px;
    font-weight: 300;
    font-size: 31px;
    line-height: 34px;
    color: var(--navy);
  }
  .cta-link {
    position: absolute;
    left: 109px;
    top: 448px;
    width: 508px;
    height: 58px;
    background: var(--brand-blue);
    border-radius: 3px;
    color: var(--white);
    font-weight: 400;
    font-size: 23px;
    letter-spacing: 2px;
    display: flex;
    align-items: center;
    justify-content: center;
    text-decoration: none;
  }
</style>
</head>
<body>
  <div class="board-title">PREVIEW</div>

  <div class="banner-frame first">
    <div class="banner">
      <svg class="banner-shapes" viewBox="0 0 1570 655" width="1570" height="655">
        <defs>
          <linearGradient id="blueWedgeA" x1="0" y1="0" x2="0" y2="1">
            <stop offset="0" stop-color="#0072d0"/>
            <stop offset="1" stop-color="#002a70"/>
          </linearGradient>
          <linearGradient id="photoToneA" x1="0" y1="0" x2="1" y2="1">
            <stop offset="0" stop-color="#6b5a4a"/>
            <stop offset="0.45" stop-color="#3a4150"/>
            <stop offset="1" stop-color="#c8ccd4"/>
          </linearGradient>
        </defs>
        <rect x="0" y="0" width="36" height="655" fill="#00205b"/>
        <rect x="0" y="209" width="36" height="129" fill="#0077d4"/>
        <polygon points="824,0 864,0 1178,45 926,82 926,555 1200,603 864,655 824,655" fill="url(#blueWedgeA)"/>
        <polygon points="926,82 1570,0 1570,655 926,557" fill="#ffffff"/>
        <polygon role="img" aria-label="Photo: a hand holding a pen over financial charts and a calculator on a desk" points="941,95 1566,18 1566,650 941,545" fill="url(#photoToneA)"/>
      </svg>
      <div class="brand">
        <div class="brand-square"></div>
        <div class="brand-name">
          <span>QL Private Wealth</span>
          <span>Management</span>
          <span class="gap">Oliver Brandt</span>
          <span>&amp; Associates</span>
        </div>
      </div>
      <h1 class="headline">
        <span class="headline-lead">Need a holistic</span>
        <span class="headline-main">Financial plan?</span>
      </h1>
      <div class="headline-rule"></div>
      <p class="subline">We create synchronized financial plans<br>designed for you and your family</p>
      <a class="cta-link" href="https://bookings.qvnfinancial-demo.net/calendar/OliverBrandtAssociatesQLPrivateWealth@qvnfinancial-demo.net/bookings/">www.oliverbrandtassociates-demo.ca/</a>
    </div>
  </div>

  <div class="banner-frame second">
    <div class="banner">
      <svg class="banner-shapes" viewBox="0 0 1570 655" width="1570" height="655">
        <defs>
          <linearGradient id="blueWedgeB" x1="0" y1="0" x2="0" y2="1">
            <stop offset="0" stop-color="#0072d0"/>
            <stop offset="1" stop-color="#002a70"/>
          </linearGradient>
          <linearGradient id="photoToneB" x1="0" y1="0" x2="1" y2="1">
            <stop offset="0" stop-color="#f2ead8"/>
            <stop offset="0.5" stop-color="#c9cfd8"/>
            <stop offset="1" stop-color="#2c3b5e"/>
          </linearGradient>
        </defs>
        <rect x="0" y="0" width="36" height="655" fill="#00205b"/>
        <rect x="0" y="209" width="36" height="129" fill="#0077d4"/>
        <polygon points="824,0 864,0 1178,45 926,82 926,555 1200,603 864,655 824,655" fill="url(#blueWedgeB)"/>
        <polygon points="926,82 1570,0 1570,655 926,557" fill="#ffffff"/>
        <polygon role="img" aria-label="Photo: a businessman in a suit writing on financial reports at a bright office desk" points="941,95 1566,18 1566,650 941,545" fill="url(#photoToneB)"/>
      </svg>
      <div class="brand">
        <div class="brand-square"></div>
        <div class="brand-name">
          <span>QL Private Wealth</span>
          <span>Management</span>
          <span class="gap">Oliver Brandt</span>
          <span>&amp; Associates</span>
        </div>
      </div>
      <h2 class="headline">
        <span class="headline-lead">Need a holistic</span>
        <span class="headline-main">Financial plan?</span>
      </h2>
      <div class="headline-rule"></div>
      <p class="subline">We create synchronized financial plans<br>designed for you and your family</p>
      <a class="cta-link" href="https://bookings.qvnfinancial-demo.net/calendar/OliverBrandtAssociatesQLPrivateWealth@qvnfinancial-demo.net/bookings/">www.oliverbrandtassociates-demo.ca/</a>
    </div>
  </div>
</body>
</html>
```